Business Card for Brevel Coatings

We need a simple, yet out standing business card for our painting company.

Target Market(s)

wealthy; high-end neighborhoods, and businesses

Industry/Entity Type

Painting

Contact Information for Business Card

Name:
Doran Vask

Email:
d.vask@brevel-coatings.com

Website:
Brevel-coatings.com

Phone Number:
(555) 416-9073

Font styles to use
Serif
Sans Serif

Requirements
Must have
• slogan "Crafting Lasting Color"
Should not have
• A title attached to the name on the card

```html
<!DOCTYPE html>
<html lang="en">
<head>
<meta charset="utf-8">
<title>Brevel Coatings – Business Card</title>
<link rel="stylesheet" href="https://fonts.googleapis.com/css2?family=Cinzel:wght@400;700&family=Crimson+Text:wght@400&display=swap">
<style>
  :root {
    --backdrop: #2f3f48;
    --card: #ffffff;
    --green-dark: #3e5a1f;
    --green-lime: #9cc23b;
    --ink: #2f3b22;
    --rule: #5a6b4a;
  }
  * { box-sizing: border-box; margin: 0; padding: 0; }
  html, body {
    width: 1200px; height: 900px; overflow: hidden;
    background: var(--backdrop);
  }
  .sheet {
    width: 1200px; height: 900px;
    display: flex; flex-direction: column; align-items: center; justify-content: center;
    gap: 50px;
  }
  .card {
    position: relative;
    width: 620px; height: 355px;
    background: var(--card);
    box-shadow: 0 10px 24px rgba(0,0,0,.35);
    overflow: hidden;
  }

  /* Front */
  .card--front {
    display: flex; flex-direction: column; align-items: center; justify-content: center;
    gap: 16px;
  }
  .brand { display: flex; align-items: center; gap: 14px; }
  .brand__dot {
    width: 40px; height: 40px; border-radius: 50%;
    background: var(--green-lime);
    flex: none;
  }
  .brand__name {
    font-family: "Cinzel", serif;
    font-weight: 700;
    color: var(--green-dark);
    font-size: 42px;
    letter-spacing: 1px;
    line-height: 1;
  }
  .slogan {
    font-family: "Cinzel", serif;
    font-weight: 400;
    color: var(--green-lime);
    font-size: 17px;
    letter-spacing: 5px;
  }

  /* Back */
  .card--back {
    display: flex; align-items: center;
    padding: 0 40px 60px 46px;
  }
  .card--back .brand { gap: 10px; width: 268px; }
  .card--back .brand__dot { width: 28px; height: 28px; }
  .card--back .brand__name { font-size: 33px; line-height: 1.05; }
  .divider {
    width: 1px; height: 128px; background: var(--rule);
    margin: 0 16px 0 14px;
  }
  .contact { display: flex; flex-direction: column; gap: 11px; }
  .contact__name {
    font-family: "Cinzel", serif; font-weight: 700;
    color: var(--green-dark); font-size: 21px; margin-bottom: 4px;
  }
  .contact__row {
    display: flex; align-items: center; gap: 10px;
    font-family: "Crimson Text", serif; font-size: 15px; color: var(--ink);
  }
  .contact__row svg { width: 18px; height: 18px; flex: none; }
  .band-lime {
    position: absolute; left: 0; right: 0; bottom: 40px; height: 6px;
    background: var(--green-lime);
  }
  .band-dark {
    position: absolute; left: 0; right: 0; bottom: 0; height: 32px;
    background: var(--green-dark);
  }
</style>
</head>
<body>
<main class="sheet">
  <section class="card card--front" aria-label="Card front">
    <div class="brand">
      <span class="brand__dot"></span>
      <span class="brand__name">Brevel Coatings</span>
    </div>
    <p class="slogan">Crafting Lasting Color</p>
  </section>

  <section class="card card--back" aria-label="Card back">
    <div class="brand">
      <span class="brand__dot"></span>
      <span class="brand__name">Brevel Coatings</span>
    </div>
    <span class="divider"></span>
    <div class="contact">
      <p class="contact__name">Doran Vask</p>
      <p class="contact__row">
        <svg viewBox="0 0 24 24" aria-hidden="true"><path fill="#3e5a1f" d="M6.6 10.8a15.1 15.1 0 0 0 6.6 6.6l2.2-2.2c.3-.3.7-.4 1-.2 1.1.4 2.3.6 3.6.6.6 0 1 .4 1 1V20c0 .6-.4 1-1 1A17 17 0 0 1 3 4c0-.6.4-1 1-1h3.5c.6 0 1 .4 1 1 0 1.3.2 2.5.6 3.6.1.3 0 .7-.2 1z"/></svg>
        (555) 416-9073
      </p>
      <p class="contact__row">
        <svg viewBox="0 0 24 24" aria-hidden="true"><rect x="2.5" y="5" width="19" height="14" fill="none" stroke="#3e5a1f" stroke-width="1.8"/><path d="M2.5 5l9.5 8 9.5-8" fill="none" stroke="#3e5a1f" stroke-width="1.8"/></svg>
        d.vask@brevel-coatings.com
      </p>
      <p class="contact__row">
        <svg viewBox="0 0 24 24" aria-hidden="true"><g fill="none" stroke="#3e5a1f" stroke-width="1.6"><circle cx="12" cy="12" r="9.5"/><ellipse cx="12" cy="12" rx="4.2" ry="9.5"/><path d="M2.5 12h19M4 7h16M4 17h16"/></g></svg>
        www.brevel-coatings.com
      </p>
    </div>
    <span class="band-lime"></span>
    <span class="band-dark"></span>
  </section>
</main>
</body>
</html>
```